Flyer Design for Business: "Velvet Glow"

My Business name is "VELVET GLOW"

Laser Hair Removal
Non invasive and pain free
Look amazing and feel confident with a Hair Free body
Now is the time to start don't delay
1 treatment a month will ensure you are bikini hot for the summer months
Take full advantage of our OPENING SPECIALS of 30%-40% savings
Part payments available

CELLULITE & FAT REDUCTION
Now you too can look amazing without invasive surgery, downtime or discomfort
Tara Wellbrook & Monica Farrowdale are avid recipients of this treatment.
Effective on all skin types and delivers fast measurable results for:
Helping mums regain their pre-baby figures
Losing the love handles (but keeping the love)
Stretch mark reduction
Skin tightening
Cellulite busting on Arms, tummy, thighs.
Man boob reduction.
Latest technology:
Bi Polar radio frequency (RF)
infrared light
negative pressure (Vacuum)
Tissue manipulation through roller mechanical massage.
50% saving Call now

PDT LED REJUVENATION LIGHT THERAPY
ORVA Researchers found:
Fibroblast and muscles grew 5 times faster, stimulates
reconstruction of collagenous fibres of the dermis
These findings and more assist with:
Remove freckles, sunburn pigmentation,
Cures acne and hair follicle inflammation
Anti aging skin tightening
Reduces pore size
Improve the skin texture
Improves circulation
Red light : reduces pore size, softens skin wrinkles,reduces acne
Blue light: Kills the acne bacillus to eliminate acne, inhibit inflammation
Yellow light: Skin tightening, whitening and softens skin wrinkles
Purple light: combination of red & blue lights treats acne scars
Orange light increases cell energy and accelerates metabolism
$55 Saving and relax under the lights.

Who can resist a soothing Hot stone massage therapy after:
A hard stressful day at work
Aches and muscular pain

Pick anything from this info with a couple of nice images.

Target Market(s)

Females & males Sports minded people cyclists

Industry/Entity Type

Beauty Salon

Colors
00a990
e34197

Requirements
Must have
• a couple of images and
Nice to have
• Pink and bluey green like my business card

```html
<!DOCTYPE html>
<html lang="en">
<head>
<meta charset="utf-8">
<title>Velvet Glow – Flyer</title>
<link href="https://fonts.googleapis.com/css2?family=Lobster&family=Oswald:wght@400;500&family=Open+Sans:wght@400;600;700&display=swap" rel="stylesheet">
<style>
:root{
  --stage:#d3d3d4;
  --label:#8a8a8c;
  --white:#ffffff;
  --plum:#b24fa2;
  --plum-deep:#b86aab;
  --pink-band:#d5a2cc;
  --teal:#2bbba8;
  --teal-soft:#89d1c5;
  --teal-text:#17a08c;
  --teal-dark:#0f7f70;
}
*{margin:0;padding:0;box-sizing:border-box}
html,body{width:1200px;height:849px;overflow:hidden;background:var(--stage)}
body{position:relative;font-family:"Open Sans",Arial,sans-serif}
.side-label{position:absolute;top:20px;font:italic 400 32px/1 "Open Sans",Arial,sans-serif;color:var(--label)}
.flyer{position:absolute;top:68px;width:525px;height:744px;background:var(--white);overflow:hidden}
.flyer--front{left:52px}
.flyer--back{left:623px}
.abs{position:absolute}
.script{font-family:"Lobster",cursive}
.caps{font-family:"Oswald",Arial,sans-serif;text-transform:uppercase}
.figures{position:absolute;border-radius:40px;background:linear-gradient(110deg,#c46bb8 0%,#dca2d3 48%,#8fd9cb 52%,#7fd3c5 100%);opacity:.85}
.figures--front{left:14px;top:14px;width:200px;height:222px}
.figures--back{left:326px;top:22px;width:170px;height:176px}
.brand-name{display:flex;align-items:center;gap:7px;font:700 17px/1 "Open Sans",Arial,sans-serif;color:var(--plum);white-space:nowrap}
.brand-name::before{content:"";width:12px;height:12px;border-radius:50%;background:var(--teal);flex:none}
.brand-name--front{left:40px;top:246px}
.brand-name--back{left:290px;top:206px;font-size:22px}
.headline{left:232px;top:30px;font-size:33px;line-height:45px;color:var(--plum)}
.nurse{left:200px;top:144px;width:310px;text-align:center;font:15px/27px "Lobster",cursive;color:var(--teal-text)}
.disclaimer{left:188px;top:254px;font:400 9.5px/1 "Oswald",sans-serif;color:var(--plum);text-transform:uppercase}
.band{position:absolute;left:0;width:100%}
.band--laser{top:284px;height:140px;background:var(--pink-band)}
.band--cellulite{top:440px;height:304px;background:var(--teal)}
.band-title{width:100%;text-align:center;color:var(--white);font-size:21px}
.band-copy{width:100%;text-align:center;color:var(--white);font-size:11.2px;line-height:17px}
.band-copy .caps{font-size:15px;font-weight:500}
.checklist{list-style:none;color:var(--white);font-size:11.4px;line-height:17px}
.checklist li{position:relative;padding-left:16px}
.checklist li::before{content:"";position:absolute;left:0;top:3.5px;width:10px;height:10px;border-radius:50%;background:#eef7f5}
.bubble{position:absolute;border-radius:50%;background:radial-gradient(circle at 45% 30%,#f0d8ec 0%,#d3a3cb 55%,#c68fbd 100%);display:flex;flex-direction:column;align-items:center;justify-content:center;color:var(--white);text-align:center}
.bubble--call{left:348px;top:541px;width:148px;height:148px;transform:rotate(6deg)}
.bubble--call b{font:500 34px/1 "Oswald",sans-serif}
.bubble--call i{font:500 26px/1.05 "Oswald",sans-serif;font-style:normal;text-transform:uppercase}
.contact{left:24px;display:flex;align-items:center;gap:12px;font-size:19px;color:var(--plum)}
.contact svg{width:22px;height:22px;flex:none}
.watch{left:378px;top:16px;width:100px;height:100px;transform:rotate(-14deg)}
.watch span{font:18px/20px "Lobster",cursive}
.pointer{position:absolute;left:0;top:212px}
.band--light{top:264px;height:308px;background:var(--teal-soft)}
.band--stone{top:587px;height:95px;background:var(--plum-deep)}
.light-copy{color:var(--teal-dark);font-size:11.2px;line-height:17px;text-align:center;font-weight:600}
.checklist--dark{color:var(--teal-dark);font-weight:600;font-size:11.2px;line-height:16.8px}
.bubble--save{left:360px;top:346px;width:118px;height:118px;transform:rotate(14deg)}
.bubble--save span{font:500 17px/1.1 "Oswald",sans-serif;text-transform:uppercase}
.bubble--save small{font:400 11px/1.2 "Oswald",sans-serif;text-transform:uppercase}
.stone-q{font:500 13px/1 "Oswald",sans-serif;color:#e3c4de;text-transform:uppercase;text-align:center;width:100%}
.stone-items{display:flex;justify-content:center;gap:18px;color:var(--white);font-size:12px;font-weight:600}
.stone-items span::before{content:"";display:inline-block;width:10px;height:10px;border-radius:50%;background:#e3c4de;margin-right:6px;vertical-align:-1px}
.site{left:0;top:690px;width:100%;text-align:center;font:500 38px/1 "Oswald",sans-serif;color:var(--teal)}
</style>
</head>
<body>
<span class="side-label" style="left:52px">front</span>
<span class="side-label" style="left:627px">back</span>

<section class="flyer flyer--front">
  <div class="figures figures--front" role="img" aria-label="Illustration of a female and a male body silhouette in pink and teal"></div>
  <p class="abs brand-name brand-name--front">Velvet Glow</p>
  <h1 class="abs script headline">Body Treatments*<br>from Head to toe</h1>
  <p class="abs nurse">The main Medical Aesthetician has a<br>Nursing background of 12yrs<br>and is also a Registered Nurse .</p>
  <p class="abs disclaimer">*All treatments are safe painless and effective using the latest technology.</p>

  <div class="band band--laser">
    <h2 class="abs script band-title" style="top:12px">Laser Hair Removal</h2>
    <p class="abs band-copy" style="top:42px">Non invasive and pain free<br>Look amazing and feel confident with a Hair Free body<br>Now is the time to start don't delay<br>1 treatment a month will ensure you are bikini hot for the summer months<br>Take full advantage of our <span class="caps">Opening Specials</span> of <span class="caps">30%-40% savings</span></p>
  </div>

  <div class="band band--cellulite">
    <h2 class="abs script band-title" style="top:10px">Cellulite &amp; Fat Reduction</h2>
    <p class="abs band-copy" style="top:36px">Now you too can look amazing without invasive surgery, downtime or discomfort<br>Tara Wellbrook &amp; Monica Farrowdale are avid recipients of this treatment.</p>
    <p class="abs caps" style="left:56px;top:78px;color:var(--white);font-size:15px">Effective on all skin types and delivers fast measurable results for:</p>
    <ul class="abs checklist" style="left:40px;top:100px">
      <li>Helping mums regain their pre-baby figures</li>
      <li>Losing the love handles (but keeping the love)</li>
      <li>Stretch mark reduction</li>
      <li>Skin tightening</li>
      <li>Cellulite busting on Arms, tummy, thighs.</li>
      <li>Man boob reduction.</li>
      <li>Latest technology:</li>
      <li>Bi Polar radio frequency (RF)</li>
      <li>Infrared light</li>
      <li>Negative pressure (Vacuum)</li>
      <li>Tissue manipulation through roller mechanical massage.</li>
    </ul>
  </div>
  <div class="bubble bubble--call"><b>50%</b><i>Saving</i><i>Call now</i></div>
</section>

<section class="flyer flyer--back">
  <p class="abs contact" style="top:46px"><svg viewBox="0 0 22 22"><circle cx="11" cy="11" r="11" fill="var(--teal)"/><path d="M7 6c1-1 2 0 2.5 1.5s-1 1.5-.5 2.5 1.5 2 2.5 2.5 1-1 2.5-.5S16 14 15 15s-4 0-6-2-3-5-2-7z" fill="#fff"/></svg><span class="script">0491 570 326</span></p>
  <p class="abs contact" style="top:82px"><svg viewBox="0 0 22 22"><circle cx="11" cy="11" r="11" fill="var(--teal)"/><text x="11" y="15.5" text-anchor="middle" font-size="14" font-family="Arial" font-weight="700" fill="#fff">@</text></svg><span class="script">hello@velvetglowmail.com</span></p>
  <p class="abs contact" style="top:118px;align-items:flex-start"><svg viewBox="0 0 22 22" style="margin-top:4px"><circle cx="11" cy="11" r="11" fill="var(--teal)"/><g fill="none" stroke="#fff" stroke-width="1.3"><circle cx="11" cy="11" r="6.5"/><ellipse cx="11" cy="11" rx="3" ry="6.5"/><path d="M4.5 11h13"/></g></svg><span class="script" style="line-height:30px">Suite 4.02, 18 Harlow Parade,<br>Brimsdale NSW 2571</span></p>

  <div class="figures figures--back" role="img" aria-label="Illustration of a female and a male body silhouette in pink and teal"></div>
  <div class="bubble watch"><span>Watch<br>for our<br>Specials</span></div>
  <svg class="pointer" width="276" height="20" viewBox="0 0 276 20"><path d="M0 2h264l10 8-10 8H0z" fill="var(--pink-band)"/></svg>
  <p class="abs brand-name brand-name--back">Velvet Glow</p>

  <div class="band band--light">
    <h2 class="abs script band-title" style="top:12px;font-size:20px">Pdt Led Rejuvenation Light Therapy</h2>
    <p class="abs light-copy" style="left:0;width:100%;top:44px">ORVA Researchers found that fibroblast and muscles grew 5 times faster, stimulates<br>reconstruction of collagenous fibres of the dermis</p>
    <p class="abs caps" style="left:80px;top:86px;color:var(--teal-dark);font-size:13.5px">These findings and more assist with:</p>
    <ul class="abs checklist checklist--dark" style="left:66px;top:107px">
      <li>Remove freckles, sunburn pigmentation,</li>
      <li>Cures acne and hair follicle inflammation</li>
      <li>Anti aging skin tightening</li>
      <li>Reduces pore size</li>
      <li>Improve the skin texture</li>
      <li>Improves circulation</li>
      <li>Red light : reduces pore size, softens skin wrinkles,reduces acne</li>
      <li>Blue light: Kills the acne bacillus to eliminate acne, inhibit inflammation</li>
      <li>Yellow light: Skin tightening, whitening and softens skin wrinkles</li>
      <li>Purple light: combination of red &amp; blue lights treats acne scars</li>
      <li>Orange light increases cell energy and accelerates metabolism</li>
    </ul>
  </div>
  <div class="bubble bubble--save"><span>$55 saving<br>and relax</span><small>under the lights.</small></div>

  <div class="band band--stone">
    <h2 class="abs script band-title" style="top:8px;font-size:20px">Hot Stone Massage</h2>
    <p class="abs stone-q" style="top:44px">Who can resist a soothing hot stone massage therapy after?</p>
    <p class="abs stone-items" style="left:0;width:100%;top:64px"><span>A hard stressful day at work</span><span>Aches and muscular pain</span></p>
  </div>
  <p class="abs site">VELVETGLOW.COM.AU</p>
</section>
</body>
</html>
```